Brightvale Crew Word Press Website

We need a graphical, fun website that conveys our messaging of providing the Best-In-Class Signature Marketing System for Mortgage Loan Officers and Realtors. Our system uses AI and Predictive Analysis to uncover the 'Gold' hidden in contact databases. The 'Gold' is defined as people who are in the market or likely to be in the market soon. We place that 'Gold' in the form of Contact Name, Address, Phone and Email on a Daily To Do List detailing what type of contact should be made.

Target Market(s)

Mortgage Loan Officers and Realtors

Industry/Entity Type

Mortgage & Real Estate

Coding

Coded - Design and coding required

Number of Pages Required

5+ page

Requirements
Must have
• I like the look of this site- https://www.homeloanpromostudio.example/
Nice to have
• Please create a flow that is similar to https://www.homeloanpromostudio.example/, but better, more dynamic. Site must be responsive and mobile friendly. Site will have embedded videos. Site need to convey a message of hope, imagination, innovation, results oriented, better than the rest, victory!
Should not have
• Nothing cheesy or low class.

```html
<!DOCTYPE html>
<html lang="en">
<head>
<meta charset="utf-8">
<title>Brightvale Crew — Signature Marketing System</title>
<link href="https://fonts.googleapis.com/css2?family=Poppins:wght@300;400;500;600;700&display=swap" rel="stylesheet">
<style>
:root{
  --black:#000;
  --dark-1:#262626;
  --dark-2:#0d0d0d;
  --ink:#1c1c1c;
  --muted:#6d6d6d;
  --gold-1:#e0b834;
  --gold-2:#a7841f;
  --blue:#1583c4;
  --teal:#17c2a0;
  --cream:#fff6df;
  --ice:#e6f4fb;
  --white:#fff;
}
*{box-sizing:border-box;margin:0;padding:0}
html,body{width:1200px;height:4051px;overflow:hidden;background:var(--white)}
body{position:relative;font-family:'Poppins',sans-serif;color:var(--ink)}
.backdrop{position:absolute;left:0;top:0}
.abs{position:absolute}
.brand{display:flex;align-items:center;gap:8px;font-weight:600;color:var(--gold-1);font-size:17px}
.brand-dot{width:12px;height:12px;border-radius:50%;background:var(--gold-1)}
.nav a{position:absolute;color:var(--white);font-size:10px;font-weight:600;text-decoration:none}
.heading{font-weight:300;letter-spacing:-.2px;white-space:nowrap}
.heading b{font-weight:600}
.copy{font-size:10px;line-height:20px;color:var(--muted)}
.on-dark{color:var(--white)}
.copy.on-dark{color:#cfcfcf}
.btn{display:inline-flex;align-items:center;justify-content:center;gap:5px;height:33px;padding:0 18px;border-radius:4px;background:linear-gradient(90deg,var(--gold-1),var(--gold-2));color:var(--white);font-size:9px;font-weight:600;text-decoration:none}
.btn svg{width:12px;height:8px}
.art{border-radius:16px}
.cards{display:flex;gap:33px}
.card{width:201px;height:288px;border-radius:8px;text-align:center;padding-top:22px;color:var(--ink)}
.card.cream{background:linear-gradient(180deg,#fff 0%,var(--cream) 100%)}
.card.ice{background:linear-gradient(180deg,#fff 0%,var(--ice) 100%)}
.card-icon{width:82px;height:82px;border-radius:50%;margin:0 auto}
.cream .card-icon{background:radial-gradient(circle,#ffe39a,#fff1cc)}
.ice .card-icon{background:radial-gradient(circle,#b9e2f6,#e6f4fb)}
.card h3{font-size:12px;font-weight:600;margin-top:27px;color:var(--ink)}
.card p{font-size:9px;line-height:15px;color:var(--muted);padding:0 18px;margin-top:10px}
.card .btn{height:30px;margin-top:18px;padding:0 18px}
.field{width:312px;height:34px;border:1px solid var(--gold-2);border-radius:4px;color:#9a9a9a;font-size:10px;padding:0 14px;display:flex;align-items:center}
.footer-nav a{position:absolute;font-size:11px;font-weight:500;color:var(--ink);text-decoration:none}
.sep{position:absolute;width:1px;height:12px;background:#c9c9c9}
.rule{position:absolute;height:1px;background:#e6e6e6}
</style>
</head>
<body>

<svg class="backdrop" width="1200" height="4051" viewBox="0 0 1200 4051" aria-hidden="true">
  <defs>
    <linearGradient id="goldLine" x1="0" x2="1">
      <stop offset="0" stop-color="#a7841f"/><stop offset=".5" stop-color="#e8c55a"/><stop offset="1" stop-color="#c49a27"/>
    </linearGradient>
    <linearGradient id="darkBand" x1="0" y1="0" x2="1" y2="1">
      <stop offset="0" stop-color="#2a2a2a"/><stop offset="1" stop-color="#0a0a0a"/>
    </linearGradient>
  </defs>
  <polygon points="0,0 1200,0 1200,586 0,676" fill="#000"/>
  <line x1="0" y1="680" x2="1200" y2="590" stroke="url(#goldLine)" stroke-width="6"/>
  <polygon points="0,1348 1200,1348 1200,1996 0,2088" fill="url(#darkBand)"/>
  <line x1="0" y1="2092" x2="1200" y2="2000" stroke="url(#goldLine)" stroke-width="6"/>
  <polygon points="0,3060 1200,2973 1200,3579 0,3665" fill="url(#darkBand)"/>
  <line x1="0" y1="3668" x2="1200" y2="3582" stroke="url(#goldLine)" stroke-width="6"/>
</svg>

<header>
  <div class="abs brand" style="left:140px;top:24px"><span class="brand-dot"></span>Brightvale Crew</div>
  <nav class="nav">
    <a href="#" style="left:868px;top:29px">About</a>
    <a href="#" style="left:930px;top:29px">Service</a>
    <a href="#" style="left:1000px;top:29px">Contact us</a>
  </nav>
</header>

<section class="hero">
  <h1 class="abs heading on-dark" style="left:148px;top:182px;font-size:22px;line-height:34px">The Best-In-Class Signature<br>Marketing <b>System For Mortgage<br>Loan Officers And Realtors</b></h1>
  <p class="abs copy on-dark" style="left:148px;top:296px;width:300px">Glintmark is a results-driven content marketing agency. Simply put – we drive organic traffic growth for today's top brands.</p>
  <a class="abs btn" href="#" style="left:148px;top:382px;width:107px">Contact us <svg viewBox="0 0 12 8"><path d="M0 4h11M8 1l3 3-3 3" stroke="#fff" fill="none"/></svg></a>
  <div class="abs art" role="img" aria-label="Illustration of a row of colourful houses with clouds and charts" style="left:540px;top:189px;width:613px;height:340px;background:linear-gradient(120deg,#1b1b1b 0%,#c49a27 35%,#1583c4 60%,#f5efe0 85%,#17c2a0 100%);opacity:.9"></div>
</section>

<section class="traffic">
  <h2 class="abs heading" style="left:0;width:1200px;text-align:center;top:728px;font-size:27px">Get More Traffic. &nbsp;<b>Get More Loans!</b></h2>
  <p class="abs copy" style="left:420px;width:360px;text-align:center;top:776px">Glintmark is a results-driven content marketing agency. Simply put – we drive organic traffic growth for today's top brands.</p>
  <a class="abs btn" href="#" style="left:546px;top:841px;width:107px">Contact us <svg viewBox="0 0 12 8"><path d="M0 4h11M8 1l3 3-3 3" stroke="#fff" fill="none"/></svg></a>
  <div class="abs art" role="img" aria-label="Illustration of three smiling team members in front of a browser window with house icons" style="left:280px;top:920px;width:660px;height:428px;border-radius:16px 16px 0 0;background:linear-gradient(180deg,#f3f9fc 0%,#d6ecf7 45%,#e6c25a 70%,#1583c4 100%)"></div>
</section>

<section class="services">
  <h2 class="abs heading on-dark" style="left:0;width:1200px;text-align:center;top:1420px;font-size:27px;line-height:39px">The Best-In-Class Signature<br>Marketing <b>System For Mortgage<br>Loan Officers And Realtors</b></h2>
  <div class="abs cards" style="left:148px;top:1614px">
    <article class="card cream">
      <div class="card-icon" role="img" aria-label="Brand design icon"></div>
      <h3>Brand Design &amp; Strategy</h3>
      <p>But I must explain to you how all this mistaken idea of denouncing pleasure and praising pain was born and I</p>
      <a class="btn" href="#">Learn more <svg viewBox="0 0 12 8"><path d="M0 4h11M8 1l3 3-3 3" stroke="#fff" fill="none"/></svg></a>
    </article>
    <article class="card ice">
      <div class="card-icon" role="img" aria-label="Reputation management icon"></div>
      <h3>Reputation Management</h3>
      <p>But I must explain to you how all this mistaken idea of denouncing pleasure and praising pain was born and I</p>
      <a class="btn" href="#">Learn more <svg viewBox="0 0 12 8"><path d="M0 4h11M8 1l3 3-3 3" stroke="#fff" fill="none"/></svg></a>
    </article>
    <article class="card cream">
      <div class="card-icon" role="img" aria-label="Mortgage chatbot icon"></div>
      <h3>Mortgage Chatbot</h3>
      <p>But I must explain to you how all this mistaken idea of denouncing pleasure and praising pain was born and I</p>
      <a class="btn" href="#">Learn more <svg viewBox="0 0 12 8"><path d="M0 4h11M8 1l3 3-3 3" stroke="#fff" fill="none"/></svg></a>
    </article>
    <article class="card ice">
      <div class="card-icon" role="img" aria-label="Content marketing icon"></div>
      <h3>Content Marketing</h3>
      <p>But I must explain to you how all this mistaken idea of denouncing pleasure and praising pain was born and I</p>
      <a class="btn" href="#">Learn more <svg viewBox="0 0 12 8"><path d="M0 4h11M8 1l3 3-3 3" stroke="#fff" fill="none"/></svg></a>
    </article>
  </div>
</section>

<section class="brokers">
  <h2 class="abs heading" style="left:160px;top:2184px;font-size:28px;line-height:40px">Mortgage Brokers Have More<br>Options And Better <b>Prices And<br>Service But Are At A Competitive<br>Disadvantage</b></h2>
  <p class="abs copy" style="left:160px;top:2356px;width:360px">Glintmark is a results-driven content marketing agency. Simply put – we drive organic traffic growth for today's top brands.</p>
  <a class="abs btn" href="#" style="left:160px;top:2420px;width:107px">Contact us <svg viewBox="0 0 12 8"><path d="M0 4h11M8 1l3 3-3 3" stroke="#fff" fill="none"/></svg></a>
  <div class="abs art" role="img" aria-label="Illustration of a busy broker juggling documents, laptop and house icons" style="left:692px;top:2171px;width:428px;height:346px;background:radial-gradient(circle at 55% 50%,#1583c4 0%,#e6c25a 40%,#f4f8fb 72%)"></div>
</section>

<section class="growth">
  <div class="abs art" role="img" aria-label="Illustration of two people flying beside a launching rocket" style="left:157px;top:2643px;width:401px;height:314px;background:radial-gradient(circle at 50% 45%,#1583c4 0%,#17c2a0 35%,#e6c25a 55%,#f6f9fb 75%)"></div>
  <h2 class="abs heading" style="left:617px;top:2660px;font-size:28px;line-height:40px">The Best-In-Class Signature<br>Marketing <b>System For Mortgage<br>Loan Officers And Realtors</b></h2>
  <p class="abs copy" style="left:617px;top:2793px;width:360px">Glintmark is a results-driven content marketing agency. Simply put – we drive organic traffic growth for today's top brands.</p>
  <a class="abs btn" href="#" style="left:617px;top:2866px;width:107px">Contact us <svg viewBox="0 0 12 8"><path d="M0 4h11M8 1l3 3-3 3" stroke="#fff" fill="none"/></svg></a>
</section>

<section class="subscribe">
  <h2 class="abs heading on-dark" style="left:209px;top:3170px;font-size:28px;line-height:40px">Subscribe For Free<br><b>Marketing Resources</b></h2>
  <p class="abs copy on-dark" style="left:209px;top:3268px;width:320px">Glintmark is a results-driven content marketing agency. Simply put – we drive organic traffic growth for today's top brands.</p>
  <div class="abs field" style="left:209px;top:3352px">Your email</div>
  <a class="abs btn" href="#" style="left:209px;top:3403px;width:107px">Contact us <svg viewBox="0 0 12 8"><path d="M0 4h11M8 1l3 3-3 3" stroke="#fff" fill="none"/></svg></a>
  <div class="abs art" role="img" aria-label="Illustration of a blue mailbox with envelopes, newsletter and notification bell" style="left:648px;top:3130px;width:403px;height:362px;background:radial-gradient(circle at 45% 45%,#1583c4 0%,#17c2a0 30%,#c49a27 50%,#1c1c1c 75%)"></div>
</section>

<footer>
  <div class="abs brand" style="left:0;width:1200px;justify-content:center;top:3748px;font-size:22px"><span class="brand-dot"></span>Brightvale Crew</div>
  <div class="rule" style="left:315px;width:571px;top:3868px"></div>
  <nav class="footer-nav">
    <a href="#" style="left:381px;top:3901px">Home</a>
    <span class="sep" style="left:458px;top:3908px"></span>
    <a href="#" style="left:500px;top:3901px">About</a>
    <span class="sep" style="left:580px;top:3908px"></span>
    <a href="#" style="left:621px;top:3901px">Service</a>
    <span class="sep" style="left:714px;top:3908px"></span>
    <a href="#" style="left:749px;top:3901px">Contact us</a>
  </nav>
  <div class="rule" style="left:315px;width:571px;top:3948px"></div>
  <p class="abs copy" style="left:400px;width:400px;text-align:center;top:3976px;font-size:9px;line-height:15px">Copyright © 2022 Brightvale Crew. Use of this website constitutes acceptance of our User Agreement and Privacy Policy.</p>
</footer>

</body>
</html>
```